Revamp of current landing page for high conversions

I need to revamp my current landing pages and I want to see designs that incorporate elements from both of these current designs... http://www.brightmarlowsmilestudio.com/

https://qrtmno.pagewick.co/vorn-glowpackoffer77/

Please implement these images into the design: https://www.pictogram.example/p/KQX7Lm2R_Ta-/?taken-by=brightmarlowsmilestudio

https://www.pictogram.example/p/KR4WnsJdpzG/?taken-by=brightmarlowsmilestudio

https://www.pictogram.example/p/KRvqDmtk9_P/?taken-by=brightmarlowsmilestudio

https://www.pictogram.example/p/KRjemTGkRVN/?taken-by=brightmarlowsmilestudio

https://www.pictogram.example/p/KRjfa93kd-d/?taken-by=brightmarlowsmilestudio

https://www.pictogram.example/p/KReZoGTEuHa/?taken-by=brightmarlowsmilestudio

https://www.pictogram.example/p/KRThd5hkmc9/?taken-by=brightmarlowsmilestudio

https://www.pictogram.example/p/KRBksT0EcSu/?taken-by=brightmarlowsmilestudio

https://www.pictogram.example/p/KS8h5SjE8H9/?taken-by=brightmarlowsmilestudio

Target Market(s)

People that care about their looks and who want whiter teeth. People that are interested in good oral hygeine

Industry/Entity Type

Dental Clinic

Number of Pages Required

1 page

Colors

Designer to choose colors to be used in the design.

Requirements
Must have
• images of my customers that I have included in the description.
• Also, I would like to see a professional laser teeth whitening treatment that happens in dental office and make emphasis on FREE HOME MAINTENANCE KIT INCLUDED!
• Must have CALL OR TEXT 555-014-3827
Nice to have
• Must be mobile friendly responsive design-use logo from my website www.brightmarlowsmilestudo.com
Should not have
• stock images of people I dont like stock images of people so please use the images from my instagram account

```html
<!DOCTYPE html>
<html lang="en">
<head>
<meta charset="utf-8">
<title>Bright Marlow Smile Studio – $99 Laser Teeth Whitening</title>
<link href="https://fonts.googleapis.com/css2?family=Roboto:ital,wght@0,300;0,400;0,500;0,700;1,300;1,400;1,700&display=swap" rel="stylesheet">
<style>
:root{
  --blue:#00a8ec;
  --blue-dark:#0a96d6;
  --ink:#333b44;
  --muted:#6b7178;
  --white:#ffffff;
  --photo-blue:#3fb5e8;
  --photo-grey:#c9cdd1;
}
*{box-sizing:border-box;margin:0;padding:0}
html,body{width:1061px;height:1200px;overflow:hidden;background:var(--blue);font-family:'Roboto',Arial,sans-serif;color:var(--ink)}
.page{position:relative;width:1061px;height:1200px;overflow:hidden;background:var(--blue)}

.site-header{position:absolute;left:0;top:0;width:1061px;height:90px;background:var(--white);box-shadow:0 2px 6px rgba(0,0,0,.18);z-index:5}
.brand{position:absolute;left:225px;top:22px;display:flex;align-items:center;gap:10px}
.brand-mark{width:44px;height:44px;border-radius:50%;background:var(--blue)}
.brand-name{font-size:21px;font-weight:500;color:var(--ink);line-height:1.05;width:150px}
.contact{position:absolute;top:22px;text-align:center;color:var(--blue);font-size:12px;font-weight:500}
.contact svg{display:block;margin:0 auto 6px}
.contact-phone{left:612px;width:110px}
.contact-place{left:745px;width:110px}
.contact-divider{position:absolute;left:731px;top:20px;width:1px;height:48px;background:#d5d9dd}

.hero{position:absolute;left:0;top:90px;width:1061px;height:329px;background:var(--white)}
.offer{position:absolute;left:255px;top:28px;width:220px;text-align:center}
.offer-kicker{font-size:8px;color:var(--muted)}
.offer-price{display:flex;justify-content:center;align-items:center;gap:4px;margin-top:6px;color:var(--blue);font-size:56px;font-weight:700;line-height:1}
.offer-title{margin-top:12px;color:var(--blue);font-size:20px;font-weight:500;line-height:1.2}
.offer-note{margin-top:12px;font-size:8px;color:var(--ink);line-height:1.35}
.offer-call{margin-top:26px;font-size:9px;color:var(--blue);line-height:1.3}
.cta{display:inline-flex;align-items:center;gap:10px;margin-top:10px;background:var(--blue);color:var(--white);border-radius:18px;padding:8px 26px;font-size:13px;font-weight:500}
.offer-fine{margin-top:12px;font-size:7.5px;color:var(--muted)}
.customer-grid{position:absolute;left:484px;top:0;width:351px;height:329px;display:grid;grid-template-columns:repeat(3,1fr);grid-template-rows:repeat(3,1fr);gap:2px;background:#2aa6e0}
.customer-grid div{background:linear-gradient(160deg,#5cc2ec,#2d9fd8)}

.how{position:absolute;left:0;top:419px;width:1061px;height:220px;background:var(--blue);color:var(--white)}
.how h2{position:absolute;left:252px;top:16px;font-size:32px;font-weight:500}
.how-lead{position:absolute;left:252px;top:60px;width:270px;font-size:10.5px;line-height:1.3;font-style:italic;font-weight:300}
.how-lead b{font-weight:700}
.how-body{position:absolute;left:252px;top:112px;width:275px;font-size:12px;line-height:1.28;font-weight:300}

.price-card{position:absolute;left:570px;top:385px;width:215px;height:285px;background:var(--white);box-shadow:0 2px 8px rgba(0,0,0,.2);text-align:center;z-index:4;padding-top:22px}
.price-card .lead{font-size:13px;font-style:italic;font-weight:300;color:var(--muted);line-height:1.3}
.price-card .for{margin-top:6px;color:var(--blue);font-size:19px;font-weight:500}
.price-card .amount{color:var(--blue);font-size:72px;font-weight:500;line-height:1}
.price-card .save{margin-top:12px;font-size:13px;font-style:italic;font-weight:300;color:var(--ink);line-height:1.3}
.price-card .occasion{margin:16px auto 0;width:185px;font-size:8px;color:var(--ink);line-height:1.4}

.team-band{position:absolute;left:0;top:639px;width:1061px;height:216px;background:linear-gradient(90deg,#bfc3c7,#d9dcdf 50%,#c3c7cb)}

.testimonial{position:absolute;left:331px;top:700px;width:398px;height:210px;background:var(--white);border-radius:12px;box-shadow:0 2px 8px rgba(0,0,0,.25);text-align:center;z-index:4}
.quote-badge{position:absolute;left:169px;top:-34px;width:60px;height:60px;border-radius:50%;background:var(--blue);display:flex;align-items:center;justify-content:center}
.testimonial blockquote{margin:42px auto 0;width:330px;font-size:10px;font-style:italic;font-weight:300;line-height:1.4;color:var(--muted)}
.testimonial hr{width:180px;margin:14px auto 10px;border:0;border-top:1px solid #b9bec3}
.testimonial cite{font-style:normal;font-size:12px;color:var(--blue)}
.testimonial cite b{font-weight:500}

.features h2{position:absolute;left:252px;top:938px;color:var(--white);font-size:30px;font-weight:500}
.feature-labels{position:absolute;left:250px;top:1000px;width:126px;text-align:right;color:var(--white);font-size:12px}
.feature-labels li{list-style:none;height:27px;line-height:20px}
.plan{position:absolute;top:941px;width:104px;height:197px;border-radius:10px;overflow:hidden;box-shadow:0 1px 4px rgba(0,0,0,.15)}
.plan-head{height:47px;background:var(--white);border-bottom:3px solid var(--blue-dark);display:flex;align-items:center;justify-content:center;text-align:center;color:var(--blue);font-size:16px;line-height:1.05}
.plan-head.brand-head{font-size:11px;font-weight:500;color:var(--ink);gap:5px}
.plan-head.brand-head i{width:16px;height:16px;border-radius:50%;background:var(--blue);flex:none}
.plan ul{list-style:none;background:linear-gradient(180deg,#d7effa,#bfe5f6);height:150px;padding-top:10px}
.plan li{height:27px;line-height:20px;font-size:8px;padding-left:8px;color:var(--ink);background:linear-gradient(90deg,rgba(255,255,255,.9),rgba(255,255,255,.3))}
.plan li+li{border-top:2px solid rgba(0,168,236,.15)}
</style>
</head>
<body>
<div class="page">

  <header class="site-header">
    <div class="brand">
      <span class="brand-mark"></span>
      <span class="brand-name">Bright Marlow Smile Studio</span>
    </div>
    <div class="contact contact-phone">
      <svg width="24" height="24" viewBox="0 0 24 24" fill="none" stroke="currentColor" stroke-width="1.6"><path d="M5 3h4l2 5-2.5 1.5a11 11 0 0 0 6 6L16 13l5 2v4a2 2 0 0 1-2 2A16 16 0 0 1 3 5a2 2 0 0 1 2-2z"/></svg>
      1-555-014-3826
    </div>
    <span class="contact-divider"></span>
    <div class="contact contact-place">
      <svg width="24" height="24" viewBox="0 0 24 24" fill="none" stroke="currentColor" stroke-width="1.6"><path d="M12 22s7-7 7-12a7 7 0 0 0-14 0c0 5 7 12 7 12z"/><circle cx="12" cy="10" r="2.5"/></svg>
      Harbor Flats
    </div>
  </header>

  <section class="hero">
    <div class="offer">
      <p class="offer-kicker">$378 Teeth Whitening System For Only</p>
      <div class="offer-price">$99
        <svg width="44" height="44" viewBox="0 0 44 44" fill="none" stroke="currentColor" stroke-width="2.4"><rect x="4" y="7" width="30" height="26" rx="3"/><path d="M4 15h30M11 3v8M27 3v8"/><circle cx="30" cy="30" r="11" fill="#fff"/><path d="M30 24v6l4 3"/></svg>
      </div>
      <h1 class="offer-title">LASER TEETH<br>WHITENING DEAL</h1>
      <p class="offer-note">Our exclusive "Triple Treatment"<br>plus one take home maintenance kit</p>
      <p class="offer-call">Call or text to book 1-555-014-3827<br>or click below to get the deal</p>
      <a class="cta">
        <svg width="16" height="16" viewBox="0 0 16 16" fill="none" stroke="#fff" stroke-width="1.5"><circle cx="8" cy="8" r="7"/><path d="M4.5 8h7M8.5 5l3 3-3 3"/></svg>
        GET THIS DEAL NOW
      </a>
      <p class="offer-fine">* Limited Appointments available - print free coupon</p>
    </div>
    <div class="customer-grid" role="img" aria-label="Grid of nine photos of happy customers holding signs with the studio team">
      <div></div><div></div><div></div><div></div><div></div><div></div><div></div><div></div><div></div>
    </div>
  </section>

  <section class="how">
    <h2>How it Works</h2>
    <p class="how-lead"><b>Why pay hundreds of dollars</b> when you can get a professional teeth whitening procedure for much less than your local dentist office?</p>
    <p class="how-body">We utilize the latest Blue Light Whitening Technology in combination with our Hydrogen Peroxide Whitening Gel to accelerate the whitening process! It's effective, safe and affordable! With our treatment your smile will be noticeably whiter in less than an hour!</p>
  </section>

  <aside class="price-card">
    <p class="lead">Affordable Teeth Whitening<br>in Marlow Bay</p>
    <p class="for">for only</p>
    <p class="amount">$99</p>
    <p class="save">Save Hundreds vs<br>Going To Your Local Dentist!</p>
    <p class="occasion">Get ready for High School Prom, Mother's Day, Graduation, Wedding, Vacation, or any Occasion.</p>
  </aside>

  <div class="team-band" role="img" aria-label="Faded photo of the studio team and customers holding signs"></div>

  <figure class="testimonial">
    <span class="quote-badge">
      <svg width="30" height="24" viewBox="0 0 30 24" fill="#fff"><path d="M0 24V13C0 5 4 1 12 0v5c-4 1-6 3-6 7h6v12zM17 24V13c0-8 4-12 12-13v5c-4 1-6 3-6 7h6v12z"/></svg>
    </span>
    <blockquote>"So I just had my teeth whitened using the blue laser light and I have to say this was one of the best experiences I've had with teeth whitening. Marisol (the women who helped me) was very clear about the process and walked me through each ste. I would say the whole process took about 45-60 minutes. After the teeth whitening process was finished I could tell immediately and I was very pleased with the end results."</blockquote>
    <hr>
    <cite><b>Dorian K.</b> Marlow Bay, CA</cite>
  </figure>

  <section class="features">
    <h2>Features</h2>
    <ul class="feature-labels">
      <li>SPEED</li><li>EASE OF USE</li><li>COST</li><li>TIME REQUIREMENTS</li><li>AVAILABILITY</li>
    </ul>
    <div class="plan" style="left:395px">
      <div class="plan-head brand-head"><i></i>Bright Marlow</div>
      <ul><li>Results in 45 minutes</li><li>Very easy</li><li>$378</li><li>Less than an hour</li><li>Walk in &amp; By Appt</li></ul>
    </div>
    <div class="plan" style="left:506px">
      <div class="plan-head">LUMIPRO</div>
      <ul><li>Results in 3 Treatments</li><li>Difficult/Dentist</li><li>$600-$1000</li><li>3 Hours</li><li>By Apointment Only</li></ul>
    </div>
    <div class="plan" style="left:618px">
      <div class="plan-head">GLEAMWAVE</div>
      <ul><li>Results in 1 hour</li><li>Difficult/Dentist</li><li>$399-$600</li><li>1 Hour + Home Treatment</li><li>By Apointment Only</li></ul>
    </div>
    <div class="plan" style="left:729px">
      <div class="plan-head">OTHER</div>
      <ul><li>7-10 Days</li><li>Self</li><li>$50-$150</li><li>Nightly 7-30 Days</li><li>Store Purchase</li></ul>
    </div>
  </section>

</div>
</body>
</html>
```